KelvrasMassage website required

We need a website for a mobile sports massage therapist in the United Kingdom. Specialising in pregnancy and postnatal massage, sports and remedial, deep tissue massage & Corprate Massage. Attached are some logos that we already have in various colours. The file named logo_white_background is what we normally use. Feel free to use the others at your discretion.

Requirements
Must have
• Service areas, Booking system.

```html
<!DOCTYPE html>
<html lang="en">
<head>
<meta charset="utf-8">
<title>Kelvra's Massage</title>
<link href="https://fonts.googleapis.com/css2?family=Raleway:wght@400;500;600;700&family=Lato:wght@400;700&family=Prompt:wght@300;400&display=swap" rel="stylesheet">
<style>
  :root{
    --steel:#5a8ea6;
    --steel-dark:#3f6f86;
    --sky:#4fb8e8;
    --sky-soft:#9fd4ee;
    --ink:#0b0d0f;
    --panel:#1a1f24;
    --field:#2c3b48;
    --paper:#ffffff;
    --mist:#f7f7f7;
    --nav:#eef1f3;
    --text:#555a5e;
    --muted:#8a8f93;
    --sage:#8a9e86;
  }
  *{box-sizing:border-box;margin:0;padding:0}
  html,body{width:1200px;height:2400px;overflow:hidden;background:var(--paper)}
  body{position:relative;font-family:'Raleway',sans-serif;color:var(--text)}
  .abs{position:absolute}

  .top-band{left:0;top:0;width:1200px;height:520px}
  .brand{left:0;top:30px;width:1200px;text-align:center;color:#fff}
  .brand-name{font-family:'Raleway',sans-serif;font-weight:600;font-size:38px;letter-spacing:1px;line-height:1.1}
  .brand-sub{font-family:'Raleway',sans-serif;font-weight:600;font-size:14px;letter-spacing:9px;margin-top:6px}

  .site{left:75px;top:131px;width:1048px}
  .nav{left:75px;top:131px;width:1048px;height:37px;background:var(--nav);display:flex;justify-content:center;gap:26px;align-items:center;font-family:'Prompt',sans-serif;font-size:15px;color:var(--sky)}
  .nav-line{left:147px;top:165px;width:901px;height:3px;background:var(--sky-soft)}

  .hero{left:75px;top:168px;width:1048px;height:414px;background:linear-gradient(100deg,#cfcfcf 0%,#8d8d8d 30%,#e0e0e0 60%,#b5b5b5 100%)}
  .specialties{left:211px;top:227px;width:439px;height:282px;background:rgba(40,40,40,.78);padding:30px 36px}
  .spec-title{display:flex;align-items:center;gap:26px;color:#fff;font-size:28px;font-weight:500;margin-left:20px}
  .spec-title::before,.spec-title::after{content:"";width:46px;height:2px;background:#fff}
  .spec-list{list-style:none;margin-top:18px;font-family:'Prompt',sans-serif;font-size:14px;color:var(--sky);line-height:27px;padding-left:10px;letter-spacing:.5px}
  .spec-list li::before{content:"— ";}
  .spec-list li.cont::before{content:"";padding-left:13px}
  .btn-book{margin-top:26px;width:181px;height:44px;border:2px solid #ddd;border-radius:22px;color:#fff;font-family:'Raleway',sans-serif;font-style:normal;font-size:20px;letter-spacing:2px;display:flex;align-items:center;justify-content:center}

  .about{left:75px;top:582px;width:1048px;height:514px;background:var(--paper)}
  .section-title{width:1048px;text-align:center;font-size:23px;font-weight:500;color:#555;letter-spacing:1px}
  .photo{border:3px solid var(--sky-soft);box-shadow:0 0 8px rgba(79,184,232,.5)}
  .ph1{left:170px;top:716px;width:228px;height:145px;background:linear-gradient(135deg,#f0d7cc,#c9a394)}
  .ph2{left:393px;top:732px;width:228px;height:152px;background:linear-gradient(135deg,#c59a7a,#6f5140)}
  .ph3{left:195px;top:857px;width:228px;height:152px;background:linear-gradient(135deg,#a98a78,#e5d0c6)}
  .ph4{left:423px;top:858px;width:220px;height:152px;background:linear-gradient(135deg,#f4f4f4,#c8c8c8)}
  .about-copy{left:700px;top:735px;width:300px;transform:rotate(13deg);transform-origin:left top;font-family:'Prompt',sans-serif;font-weight:300;text-transform:uppercase;color:#666;font-size:15px;line-height:27px;letter-spacing:.5px}
  .about-copy h3{font-family:'Raleway',sans-serif;font-weight:700;font-size:15px;color:#444;letter-spacing:1px;margin-bottom:10px}
  .learn{display:inline-block;margin-top:14px;border:3px solid var(--steel);color:var(--sky);padding:4px 10px;font-size:14px}

  .services{left:75px;top:1096px;width:1048px;height:523px;background:var(--mist)}
  .card{width:224px;height:230px;text-align:center;padding-top:20px}
  .card.dark{background:var(--ink);color:#fff}
  .card.light{background:#f9fafb;box-shadow:0 2px 6px rgba(0,0,0,.12);color:#444}
  .card .icon{width:78px;height:78px;margin:0 auto;border:2px solid var(--sky);border-radius:50%}
  .card h4{font-size:14px;font-weight:700;margin-top:18px;letter-spacing:.5px}
  .card p{font-size:13px;line-height:22px;margin-top:10px;color:#999}
  .card.light p{color:#888}

  .booking{left:75px;top:1619px;width:1052px;height:496px;background:linear-gradient(90deg,#8a7a66 0%,#cfc5b6 35%,#e9ece4 60%,#d8dcd2 100%)}
  .booking-copy{left:131px;top:1760px;width:340px;color:#fff}
  .booking-copy h2{font-size:22px;font-weight:500;color:#3d3d3d}
  .booking-copy p{font-size:16px;line-height:23px;margin-top:18px}
  .btn-sage{margin-top:58px;width:130px;height:34px;border-radius:17px;background:var(--sage);color:#fff;font-size:14px;display:flex;align-items:center;justify-content:center;margin-left:56px}
  .appt{left:728px;top:1656px;width:330px;height:414px;background:var(--panel);padding:40px 28px 0;color:#fff}
  .appt h3{font-size:18px;font-weight:500;text-align:center;letter-spacing:.5px;padding-bottom:14px;border-bottom:1px solid #4a5258}
  .appt label{display:block;font-size:13px;color:#bbb;margin:20px 0 10px 26px}
  .select{height:38px;background:var(--field);display:flex;align-items:center;justify-content:space-between;padding:0 16px;font-size:13px;color:#cfe6f2}

  .footer{left:0;top:2115px;width:1200px;height:285px;background:#000;color:#fff}
  .social{left:77px;top:2155px;display:flex;gap:15px}
  .social span{width:37px;height:37px;border-radius:50%;background:#3a4046}
  .foot-rule{left:75px;top:2224px;width:202px;height:1px;background:#444}
  .news{left:75px;top:2240px;display:flex;align-items:center;gap:12px;font-size:15px;letter-spacing:1px}
  .foot-services{left:472px;top:2162px;font-size:15px}
  .foot-services ul{list-style:none;font-size:12px;line-height:23px;margin:10px 0 0 8px}
  .contact{left:928px;top:2152px;font-family:'Lato',sans-serif;font-size:15px}
  .contact ul{list-style:none;margin-top:16px}
  .contact li{display:flex;align-items:center;gap:16px;font-size:13px;height:33px}
  .copyright{left:0;top:2346px;width:1200px;text-align:center;font-family:'Lato',sans-serif;font-size:15px;color:#888}
</style>
</head>
<body>
  <svg class="abs top-band" viewBox="0 0 1200 520" aria-hidden="true">
    <defs>
      <linearGradient id="band" x1="0" y1="0" x2="0" y2="1">
        <stop offset="0" stop-color="#6a9bb2"/><stop offset="1" stop-color="#4f8199"/>
      </linearGradient>
    </defs>
    <path d="M0 0H1200V515C900 470 600 390 400 355C250 330 110 310 0 295Z" fill="url(#band)"/>
  </svg>

  <div class="abs brand">
    <div class="brand-name">Kelvra's</div>
    <div class="brand-sub">MASSAGE</div>
  </div>

  <nav class="abs nav">
    <span>HOME</span><span>ABOUT US</span><span>SERVICES</span><span>EVENTS &amp; NEWS</span><span>FAQS</span>
  </nav>
  <div class="abs nav-line"></div>

  <div class="abs hero" role="img" aria-label="Black and white photo of a therapist massaging a client's back"></div>
  <section class="abs specialties">
    <h1 class="spec-title">Specialties</h1>
    <ul class="spec-list">
      <li>pregnancy and postnatal massage</li>
      <li>sports and remedial</li>
      <li>deep tissue massage</li>
      <li class="cont">and Corprate Massage</li>
    </ul>
    <div class="btn-book">BOOK NOW</div>
  </section>

  <section class="abs about"></section>
  <h2 class="abs section-title" style="left:75px;top:632px">ABOUT US</h2>
  <div class="abs photo ph1" role="img" aria-label="Photo of hands massaging skin"></div>
  <div class="abs photo ph3" role="img" aria-label="Photo of a relaxed woman receiving a facial massage"></div>
  <div class="abs photo ph4" role="img" aria-label="Photo of a man stretching on the floor"></div>
  <div class="abs photo ph2" role="img" aria-label="Photo of a woman receiving a shoulder massage"></div>
  <div class="abs about-copy">
    <h3>Lorem ipsum dolor sit amet</h3>
    <p>Lorem ipsum dolor sit amet, consectetur adipiscing elit. Nunc porttitor mattis nisl, quis tincidunt risus gravida eget. Integer tincidunt leo ac lacus vulputate, eu eleifend enim aliquam.</p>
    <span class="learn">LEARN MORE</span>
  </div>

  <section class="abs services"></section>
  <h2 class="abs section-title" style="left:75px;top:1133px">OUR SERVICES</h2>
  <div class="abs card dark" style="left:149px;top:1229px">
    <div class="icon" role="img" aria-label="Pregnancy icon"></div>
    <h4>LOREM IPSUM DOLOR SIT</h4>
    <p>Lorem ipsum dolor sit amet,<br>consectetur adipiscing elit.</p>
  </div>
  <div class="abs card light" style="left:374px;top:1272px">
    <div class="icon" role="img" aria-label="Herbal mortar icon"></div>
    <h4>LOREM IPSUM DOLOR SIT</h4>
    <p>Lorem ipsum dolor sit amet,<br>consectetur adipiscing elit.</p>
  </div>
  <div class="abs card dark" style="left:600px;top:1229px">
    <div class="icon" role="img" aria-label="Massage table icon"></div>
    <h4>LOREM IPSUM DOLOR SIT</h4>
    <p>Lorem ipsum dolor sit amet,<br>consectetur adipiscing elit.</p>
  </div>
  <div class="abs card light" style="left:826px;top:1272px">
    <div class="icon" role="img" aria-label="Yoga pose icon"></div>
    <h4>LOREM IPSUM DOLOR SIT</h4>
    <p>Lorem ipsum dolor sit amet,<br>consectetur adipiscing elit.</p>
  </div>

  <div class="abs booking" role="img" aria-label="Photo of basil leaves, a bowl and massage oil on burlap"></div>
  <div class="abs booking-copy">
    <h2>Lorem ipsum dolor sit amet</h2>
    <p>Proin vel turpis a elit elementum interdum id quis tortor. Suspendisse in nibh in velit dignissim quis porttitor diam. Donec feugiat neque eu eros imperdiet viverra.</p>
    <div class="btn-sage">book now</div>
  </div>
  <form class="abs appt">
    <h3>BOOK AN APPOINTMENT</h3>
    <label>What Kind Of Service ?</label>
    <div class="select"><span>Lorem ipsum dolor sit amet</span><svg width="18" height="12" viewBox="0 0 18 12"><path d="M2 2l7 7 7-7" stroke="#5fc3f0" stroke-width="3" fill="none"/></svg></div>
    <label>With Whom ?</label>
    <div class="select"><span>Anyone Available</span><svg width="18" height="12" viewBox="0 0 18 12"><path d="M2 2l7 7 7-7" stroke="#5fc3f0" stroke-width="3" fill="none"/></svg></div>
    <label>When ?</label>
    <div class="select"><span>Select a Date</span><svg width="18" height="12" viewBox="0 0 18 12"><path d="M2 2l7 7 7-7" stroke="#5fc3f0" stroke-width="3" fill="none"/></svg></div>
  </form>

  <footer class="abs footer"></footer>
  <div class="abs social" aria-label="Social links"><span></span><span></span><span></span><span></span></div>
  <div class="abs foot-rule"></div>
  <div class="abs news">
    <svg width="36" height="34" viewBox="0 0 36 34" aria-hidden="true"><rect x="2" y="5" width="28" height="26" rx="2" fill="none" stroke="#5a7f95" stroke-width="2"/><path d="M2 12h28M9 2v6M23 2v6" stroke="#5a7f95" stroke-width="2"/><circle cx="27" cy="27" r="7" fill="#000" stroke="#5a7f95" stroke-width="2"/><path d="M24 27l2 2 4-4" stroke="#5a7f95" stroke-width="2" fill="none"/></svg>
    <span>NEWS AND EVENTS</span>
  </div>
  <div class="abs foot-services">
    <div>Our Services</div>
    <ul>
      <li>pregnancy and postnatal massage,</li>
      <li>sports and remedial, deep tissue massage</li>
      <li>Corprate Massage</li>
    </ul>
  </div>
  <div class="abs contact">
    <div>contact info</div>
    <ul>
      <li><svg width="20" height="26" viewBox="0 0 20 26"><path d="M10 1a9 9 0 0 0-9 9c0 7 9 15 9 15s9-8 9-15a9 9 0 0 0-9-9z" fill="#5a7f95"/><circle cx="10" cy="10" r="3.5" fill="#000"/></svg><b style="font-weight:700">United Kingdom</b></li>
      <li><svg width="22" height="22" viewBox="0 0 22 22"><path d="M5 2l4 5-2 3c1 3 3 5 6 6l3-2 5 4-3 4C9 21 1 13 1 4z" fill="#5a7f95"/></svg>xxxx xxx xxx</li>
      <li><svg width="22" height="16" viewBox="0 0 22 16"><rect x="1" y="1" width="20" height="14" fill="#5a7f95"/><path d="M1 1l10 8 10-8" stroke="#000" stroke-width="1.5" fill="none"/></svg>xxx xxx xxx</li>
    </ul>
  </div>
  <div class="abs copyright">COPYRIGHT © 20XX-2018 &nbsp;•&nbsp; Kelvras Massage Center • &nbsp;ALL RIGHTS RESERVED</div>
</body>
</html>
```